New Consulting Firm News PowerPoint Template

We are a new consulting firm that specializes in Veltrix Unified Planning Suite implementations in need of a new PowerPoint template. We need at least the following layouts:
• Main Cover Slide
• Agenda / Table of Contents
• Title slide for each of the agenda items leading into actual content
• Title + Content with nice bullets in the content
• Title + Sub-Title + Content with nice bullets in the content
• Title + Two Columns of Content
• Title + Sub-Title + Two Columns of Content
• Title + Three Columns of Content
• Title + Sub-Title + Three Columns of Content
• Title + Two Rows and Two Columns of Content (4 boxes)
• Title + Sub-Title + Two Rows and Two Columns of Content (4 boxes)
• Title + Blank
• Nascar Slide (Client logos arranged somehow)
• Case Study Slide
• Various infographic slides than can be used and modified would be amazing as well
Our logo has been uploaded and you can find our website here:
https://brannowadvisory.com
We would like the main theme colors to blend with our logo, but also have a variety of colors in the theme that compliment the main theme colors. Once we have selected a PowerPoint design we expect to immediately have a Word design contest and the winning PowerPoint design will likely be a heavy influence on the Word design.

Target Market(s)

CFO, CAO, VP of Finance, Controllers

Industry/Entity Type

Consulting

Font styles to use
Serif
Sans Serif

Requirements
Must have
• • Main Cover Slide
• Title + Blank
• Case Study Slide
Nice to have
• • Various infographic slides than can be used and modified would be amazing as well

```html
<!DOCTYPE html>
<html lang="en">
<head>
<meta charset="utf-8">
<title>Brannow Advisory – Presentation Template Overview</title>
<link href="https://fonts.googleapis.com/css2?family=Quicksand:wght@500;700&family=Montserrat:wght@400;500;600&display=swap" rel="stylesheet">
<style>
  :root{
    --blue:#1f6fc5;
    --blue-deep:#0b4aa8;
    --ink:#333a44;
    --muted:#7d848d;
    --grey:#d4d7dc;
    --grey-soft:#eceef1;
    --grey-dark:#6d7278;
    --bg:#000;
    --paper:#fff;
  }
  *{margin:0;padding:0;box-sizing:border-box}
  html,body{width:1200px;height:1200px;overflow:hidden;background:var(--bg)}
  body{position:relative;font-family:"Montserrat",sans-serif;color:var(--ink)}
  .slide{position:absolute;width:382px;height:214px;background:var(--paper);overflow:hidden}
  .slide > *{position:absolute}
  .col1{left:14px}.col2{left:410px}.col3{left:799px}
  .row1{top:14px}.row2{top:242px}.row3{top:470px}.row4{top:698px}.row5{top:926px}

  .footer-band{left:0;bottom:0;width:100%;height:4px;background:var(--grey-dark)}
  .footer-note{left:4px;bottom:5px;font-size:2.5px;color:var(--muted);letter-spacing:.2px}
  .page-tab{right:4px;bottom:2px;width:0;height:0;border-left:10px solid transparent;border-right:10px solid transparent;border-bottom:10px solid var(--blue)}
  .page-num{right:10px;bottom:2px;font-size:4px;color:#fff;font-weight:600}

  .brand{display:flex;align-items:center;gap:3px;font-family:"Quicksand",sans-serif;font-weight:700;color:var(--blue)}
  .brand-mark{width:5px;height:5px;background:var(--blue)}
  .brand.small{font-size:4.5px;right:6px;top:6px}
  .brand.small .brand-mark{width:4px;height:4px}

  .heading{font-family:"Quicksand",sans-serif;font-weight:700;color:var(--ink);white-space:nowrap}
  .heading em{font-style:normal;color:var(--blue)}
  .heading.flag::before{content:"";position:absolute;left:-6px;top:2px;width:3px;height:70%;background:var(--blue)}
  .heading.bar::before{content:"";position:absolute;left:-6px;top:1px;width:1.5px;height:85%;background:var(--ink)}
  .body-text{font-size:4.6px;line-height:1.55;color:var(--muted)}

  /* image areas: flat tones of the intended photography */
  .photo-light{background:linear-gradient(135deg,#e4e8ee 0%,#cfd6e0 100%)}
  .photo-paper{background:linear-gradient(160deg,#eef0f3 0%,#d6dae0 100%)}
  .photo-dart{background:linear-gradient(110deg,#141414 0%,#262626 100%)}
  .photo-lens{background:linear-gradient(135deg,#e6ebee 0%,#a9c2c4 100%)}
  .grey-block{background:var(--grey)}
  .blue-block{background:var(--blue)}

  /* faint architectural panels behind content */
  .backdrop{top:0;height:100%;background:var(--grey-soft)}

  /* covers */
  .cover-light{background:linear-gradient(120deg,#eef1f5 0%,#dce2ea 50%,#c8d1dd 100%)}
  .cover-blue{background:linear-gradient(120deg,#1466c9 0%,#0b52b4 50%,#0a3f95 100%)}
  .cover-brand{right:42px;top:54px;font-size:13px;flex-direction:column;gap:4px}
  .cover-brand .brand-mark{width:12px;height:12px}
  .cover-brand small{font-size:4px;letter-spacing:1.5px;font-weight:500}
  .cover-title{right:22px;top:120px;font-family:"Quicksand",sans-serif;font-weight:700;font-size:14.5px;color:var(--blue)}
  .cover-sub{right:22px;top:142px;width:175px;text-align:right;font-size:5px;line-height:1.6;color:var(--ink)}
  .cover-blue .brand,.cover-blue .cover-title,.cover-blue .cover-sub{color:#fff}
  .cover-blue .brand-mark{background:#fff}

  .progress{left:28px;width:147px}
  .progress .label{display:flex;justify-content:space-between;font-size:4.8px;color:var(--muted)}
  .progress .track{margin-top:3px;height:2px;background:var(--grey)}
  .progress .fill{height:2px;background:var(--blue)}

  .ring-label{font-size:5.5px;font-weight:600;color:var(--ink);width:50px;text-align:center}
  .team-card{width:64px;text-align:center}
  .team-card .pic{width:64px;height:64px;background:#c4c6c9}
  .team-card h4{margin-top:10px;font-size:6px;font-weight:600}
  .team-card p{font-size:3.8px;color:var(--muted);line-height:1.5}
  .bullet-item{left:12px;width:360px}
  .bullet-item h4{font-family:"Quicksand",sans-serif;font-size:7.5px;color:var(--blue);display:flex;align-items:center;gap:4px}
  .bullet-item h4::before{content:"";width:5px;height:5px;background:var(--blue-deep)}
  .bullet-item p{margin-left:12px;margin-top:2px;font-size:4.3px;line-height:1.6;color:var(--muted)}
</style>
</head>
<body>

<!-- Cover light -->
<section class="slide col1 row1 cover-light">
  <div role="img" aria-label="Soft grey abstract of floating cubes and network lines" style="left:0;top:0;width:190px;height:100%;background:linear-gradient(135deg,#f3f5f8 0%,#dfe4eb 100%)"></div>
  <div class="brand cover-brand"><span class="brand-mark"></span>BRANNOW<small>ADVISORY</small></div>
  <div class="cover-title">PROJECT TITLE HERE</div>
  <p class="cover-sub">Lorem ipsum dolor sit amet, consec- tetur adipiscing elit. Vivamus eget vestibulumex, ut tincidunt nisl.</p>
</section>

<!-- Cover blue -->
<section class="slide col2 row1 cover-blue">
  <div class="brand cover-brand"><span class="brand-mark"></span>BRANNOW<small>ADVISORY</small></div>
  <div class="cover-title">PROJECT TITLE HERE</div>
  <p class="cover-sub">Lorem ipsum dolor sit amet, consec- tetur adipiscing elit. Vivamus eget vestibulumex, ut tincidunt nisl.</p>
</section>

<!-- Pellentesque a liberor -->
<section class="slide col3 row1">
  <div class="brand small"><span class="brand-mark"></span>BRANNOW</div>
  <h2 class="heading" style="right:30px;top:30px;font-size:11.5px">Pellentesque a <em>liberor</em></h2>
  <div style="right:22px;top:30px;width:1px;height:14px;background:var(--ink)"></div>
  <div class="photo-light" role="img" aria-label="Grey 3D cubes illustration" style="left:0;top:60px;width:186px;height:97px"></div>
  <div class="blue-block" style="left:198px;top:60px;width:74px;height:97px;color:#fff;font-family:Quicksand,sans-serif;font-size:10px;line-height:1.6;padding:26px 12px">Lorem<br>ipsum<br>dolor</div>
  <div class="photo-paper" role="img" aria-label="Balance sheet with pen and calculator" style="left:284px;top:60px;width:98px;height:97px"></div>
  <p class="body-text" style="left:14px;top:170px;width:360px;font-size:4.3px">Lorem ipsum dolor sit amet, consectetur adipiscing elit. Vivamus eget vestib Lorem ipsum dolor sit amet, consectetur adipiscing elit. Vivamus eget vestib Vivamus eget vestibVivamus eget vestib</p>
  <div class="footer-band"></div><span class="footer-note">COPYRIGHT TEXT HERE</span><div class="page-tab"></div><span class="page-num">01</span>
</section>

<!-- Pellentesque habitant morbi -->
<section class="slide col1 row2">
  <div class="backdrop" style="left:240px;width:60px"></div>
  <div class="brand small"><span class="brand-mark"></span>BRANNOW</div>
  <div class="blue-block" style="left:125px;top:105px;width:46px;height:18px"></div>
  <div class="photo-paper" role="img" aria-label="Balance sheet with calculator" style="left:25px;top:28px;width:138px;height:86px"></div>
  <h2 class="heading" style="left:185px;top:33px;font-size:11px"><em>Pellentesque</em> habitant morbi</h2>
  <span style="left:172px;top:35px;color:var(--blue);font-size:9px;font-weight:700">«</span>
  <p class="body-text" style="left:185px;top:51px;width:190px">Lorem ipsum dolor sit amet, consec tetur adip- iscing elit. Vivamus eget vestibulumex, ut tincidunt pellentesque. Lorem ipsum dolor sit amet, consec tetur adip- iscing elit. Vivamus eget</p>
  <div class="grey-block" style="left:190px;top:128px;width:192px;height:80px"></div>
  <div class="photo-lens" role="img" aria-label="Magnifying glass over financial charts" style="left:218px;top:102px;width:137px;height:86px"></div>
  <div style="left:25px;top:145px;width:32px;height:1px;background:var(--ink)"></div>
  <p class="body-text" style="left:25px;top:160px;width:130px;font-size:4.2px">Lorem ipsum dolor sit amet, consec tetur adip- iscing elit. Vivamus eget vestibulumex, ut tincidunt pellentesque.</p>
  <div class="footer-band"></div><span class="footer-note">COPYRIGHT TEXT HERE</span><div class="page-tab"></div><span class="page-num">01</span>
</section>

<!-- Graphs Timeline -->
<section class="slide col2 row2">
  <div class="blue-block" style="right:0;top:0;width:24px;height:24px"></div>
  <h2 class="heading" style="left:28px;top:50px;font-size:13px"><em>Graphs</em> Timeline</h2>
  <div style="left:28px;top:72px;width:34px;height:1.5px;background:var(--ink)"></div>
  <div class="progress" style="top:114px"><div class="label"><span>Lorem Ipsum</span><span>65%</span></div><div class="track"><div class="fill" style="width:65%"></div></div></div>
  <div class="progress" style="top:140px"><div class="label"><span>Dolor Sit</span><span>88%</span></div><div class="track"><div class="fill" style="width:88%"></div></div></div>
  <div class="progress" style="top:165px"><div class="label"><span>Commodo Lectus</span><span>42%</span></div><div class="track"><div class="fill" style="width:42%"></div></div></div>
  <div class="grey-block" style="left:224px;top:66px;width:40px;height:82px"></div>
  <div class="photo-dart" role="img" aria-label="Darts hitting a dartboard bullseye" style="left:258px;top:25px;width:124px;height:166px"></div>
  <div class="blue-block" style="right:0;bottom:4px;width:24px;height:22px"></div>
  <div class="footer-band"></div><span class="footer-note">COPYRIGHT TEXT HERE</span><div class="page-tab"></div><span class="page-num">01</span>
</section>

<!-- Image Heading Here -->
<section class="slide col3 row2">
  <div class="backdrop" style="left:170px;width:60px"></div>
  <div class="brand small"><span class="brand-mark"></span>BRANNOW</div>
  <h2 class="heading bar" style="left:19px;top:32px;font-size:11.5px">Image Heading <em>Here</em></h2>
  <div class="photo-light" role="img" aria-label="Grey 3D cubes illustration" style="left:0;top:59px;width:186px;height:97px"></div>
  <div class="blue-block" style="left:186px;top:59px;width:196px;height:97px;padding:8px 10px;color:#fff">
    <h3 style="font-family:Quicksand,sans-serif;font-size:7.5px;margin-bottom:3px">Lorem ipsum dolor</h3>
    <p style="font-size:4.2px;line-height:1.55">Lorem ipsum dolor sit amet, consectetur adipiscing elit. Vivamus eget vestib Lorem ipsum dolor sit amet, consectetur adipiscing elit. Vivamus eget vestib Vivamus eget vestibVivamus eget vestib Lorem ipsum dolor sit amet.</p>
    <p style="font-size:4.2px;line-height:1.55;margin-top:4px">Vivamus eget vestib Lorem ipsum dolor sit amet, consectetur adipiscing elit. Vivamus eget vestib Vivamus eget vestibVivamus eget vestib.</p>
  </div>
  <p class="body-text" style="left:14px;top:170px;width:360px;font-size:4.3px">Lorem ipsum dolor sit amet, consectetur adipiscing elit. Vivamus eget vestib Lorem ipsum dolor sit amet, consectetur adipiscing elit. Vivamus eget vestib Vivamus eget vestibVivamus eget vestib</p>
  <div class="footer-band"></div><span class="footer-note">COPYRIGHT TEXT HERE</span><div class="page-tab"></div><span class="page-num">01</span>
</section>

<!-- Slide title rings -->
<section class="slide col1 row3">
  <div class="backdrop" style="left:300px;width:60px"></div>
  <div class="brand small"><span class="brand-mark"></span>BRANNOW</div>
  <h2 class="heading flag" style="left:11px;top:5px;font-size:9px"><em>SLIDE</em> TITLE HERE</h2>
  <svg style="left:0;top:0" width="382" height="214" viewBox="0 0 382 214">
    <g fill="none" stroke-width="3">
      <line x1="107" y1="104" x2="128" y2="104" stroke="#333a44" stroke-width="1.2"/>
      <line x1="180" y1="104" x2="201" y2="104" stroke="#333a44" stroke-width="1.2"/>
      <line x1="253" y1="104" x2="274" y2="104" stroke="#333a44" stroke-width="1.2"/>
      <circle cx="82" cy="104" r="18" stroke="#d4d7dc"/><circle cx="82" cy="104" r="18" stroke="#1f6fc5" stroke-dasharray="84.8 113.1" transform="rotate(-90 82 104)"/>
      <circle cx="155" cy="104" r="18" stroke="#d4d7dc"/><circle cx="155" cy="104" r="18" stroke="#1f6fc5" stroke-dasharray="53.2 113.1" transform="rotate(-90 155 104)"/>
      <circle cx="228" cy="104" r="18" stroke="#d4d7dc"/><circle cx="228" cy="104" r="18" stroke="#1f6fc5" stroke-dasharray="93.9 113.1" transform="rotate(-90 228 104)"/>
      <circle cx="301" cy="104" r="18" stroke="#d4d7dc"/><circle cx="301" cy="104" r="18" stroke="#1f6fc5" stroke-dasharray="73.5 113.1" transform="rotate(-90 301 104)"/>
    </g>
    <g font-family="Montserrat,sans-serif" font-size="7" font-weight="600" fill="#333a44" text-anchor="middle">
      <text x="82" y="107">75%</text><text x="155" y="107">47%</text><text x="228" y="107">83%</text><text x="301" y="107">65%</text>
    </g>
  </svg>
  <div class="ring-label" style="left:57px;top:134px">Lorem Ipsum</div>
  <div class="ring-label" style="left:130px;top:134px">Lorem Ipsum</div>
  <div class="ring-label" style="left:203px;top:134px">Lorem Ipsum</div>
  <div class="ring-label" style="left:276px;top:134px">Lorem Ipsum</div>
  <div class="footer-band"></div><span class="footer-note">COPYRIGHT TEXT HERE</span><div class="page-tab"></div><span class="page-num">01</span>
</section>

<!-- Case Studies -->
<section class="slide col2 row3">
  <div class="backdrop" style="left:320px;width:50px"></div>
  <div class="brand small"><span class="brand-mark"></span>BRANNOW</div>
  <h2 class="heading flag" style="left:10px;top:6px;font-size:10.5px">Case <em>Studies</em> Here</h2>
  <div class="photo-lens" role="img" aria-label="Magnifying glass and pen over financial report" style="left:14px;top:42px;width:118px;height:132px"></div>
  <h3 style="left:142px;top:40px;font-family:Quicksand,sans-serif;font-size:7.5px;color:var(--blue)">Case study title here</h3>
  <p class="body-text" style="left:142px;top:52px;width:228px;font-size:3.9px">Lorem ipsum dolor sit amet, consectetur adipiscing elit. Vivamus eget vestib Lorem ipsum dolor sit amet, consectetur adipiscing elit. Vivamus eget vestib Vivamus eget vestibVivamus eget vestib Lorem ipsum dolor sit amet, consectetur adipiscing elit. Vivamus eget vestib Lorem ipsum dolor sit amet.</p>
  <p class="body-text" style="left:142px;top:98px;width:228px;font-size:3.9px">Lorem ipsum dolor sit amet, consectetur adipiscing elit. Vivamus eget vestib Lorem ipsum dolor sit amet, consectetur adipiscing elit. Vivamus eget vestib Vivamus eget vestibVivamus eget vestib Lorem ipsum dolor sit amet, consectetur adipiscing elit. Vivamus eget vestib Lorem ipsum dolor sit amet.</p>
  <p class="body-text" style="left:142px;top:144px;width:228px;font-size:3.9px">Lorem ipsum dolor sit amet, consectetur adipiscing elit. Vivamus eget vestib Lorem ipsum dolor sit amet, consectetur adipiscing elit. Vivamus eget vestib Vivamus eget vestibVivamus eget vestib Lorem ipsum dolor sit amet, consectetur adipiscing elit. Vivamus eget vestib.</p>
  <div class="footer-band"></div><span class="footer-note">COPYRIGHT TEXT HERE</span><div class="page-tab"></div><span class="page-num">01</span>
</section>

<!-- Bullet Heading Here images -->
<section class="slide col3 row3">
  <h2 class="heading" style="left:12px;top:4px;font-size:11.5px">Bullet Heading <em>Here</em></h2>
  <div class="photo-light" role="img" aria-label="Grey 3D cubes illustration" style="left:16px;top:34px;width:166px;height:97px"></div>
  <div class="photo-lens" role="img" aria-label="Magnifying glass over charts" style="left:185px;top:0;width:91px;height:131px"></div>
  <div class="photo-paper" role="img" aria-label="Balance sheet with pen and calculator" style="left:284px;top:0;width:93px;height:127px"></div>
  <h3 style="left:17px;top:138px;font-family:Quicksand,sans-serif;font-size:6.5px;color:var(--blue)">Image heading here</h3>
  <p class="body-text" style="left:17px;top:147px;width:162px;font-size:3.9px">Lorem ipsum dolor sit amet, consectetur adipiscing elit. Vivamus eget vestib Lorem ipsum dolor sit amet, consectetur adipiscing elit. Vivamus eget vestib Vivamus eget vestibVivamus eget vestib Lorem ipsum dolor sit amet, consectetur adipiscing elit.</p>
  <div class="blue-block" style="left:185px;top:135px;width:191px;height:73px;padding:4px 10px;color:#fff">
    <h3 style="font-family:Quicksand,sans-serif;font-size:7px;margin-bottom:2px">Lorem ipsum dolor</h3>
    <p style="font-size:3.9px;line-height:1.55">Lorem ipsum dolor sit amet, consectetur adipiscing elit. Vivamus eget vestib Lorem ipsum dolor sit amet, consectetur adipiscing elit. Vivamus eget vestib Vivamus eget vestibVivamus eget vestib Lorem ipsum dolor sit amet, consectetur adipiscing elit. Vivamus eget vestib Lorem ipsum dolor sit amet.</p>
  </div>
  <div class="footer-band"></div><span class="footer-note">COPYRIGHT TEXT HERE</span><div class="page-tab"></div><span class="page-num">01</span>
</section>

<!-- Our Team -->
<section class="slide col1 row4">
  <div class="backdrop" style="left:230px;width:80px"></div>
  <div class="brand small"><span class="brand-mark"></span>BRANNOW</div>
  <h2 class="heading" style="left:160px;top:34px;font-size:12px">Our <em>Team</em></h2>
  <div class="blue-block" style="left:0;top:85px;width:13px;height:35px"></div>
  <div style="right:0;top:85px;width:13px;height:35px;background:var(--grey-dark)"></div>
  <div class="team-card" style="left:48px;top:72px"><div class="pic" role="img" aria-label="Team member photo placeholder"></div><h4>Lorem Ipsum</h4><p>Lorem ipsum dolor sit amet, consectetur adipiscing</p></div>
  <div class="team-card" style="left:159px;top:72px"><div class="pic" role="img" aria-label="Team member photo placeholder"></div><h4>Lorem Ipsum</h4><p>Lorem ipsum dolor sit amet, consectetur adipiscing</p></div>
  <div class="team-card" style="left:269px;top:72px"><div class="pic" role="img" aria-label="Team member photo placeholder"></div><h4>Lorem Ipsum</h4><p>Lorem ipsum dolor sit amet, consectetur adipiscing</p></div>
  <div class="footer-band"></div><span class="footer-note">COPYRIGHT TEXT HERE</span><div class="page-tab"></div><span class="page-num">01</span>
</section>

<!-- Our Location Maps -->
<section class="slide col2 row4">
  <div class="brand small"><span class="brand-mark"></span>BRANNOW</div>
  <h2 class="heading flag" style="left:11px;top:4px;font-size:9.5px"><em>Our Location</em> Maps</h2>
  <div style="left:25px;top:74px;width:1.5px;height:38px;background:var(--blue)"></div>
  <h3 class="heading" style="left:35px;top:76px;font-size:12.5px;line-height:1.55">Exercitation<br><em>ullamco laboris</em></h3>
  <p class="body-text" style="left:35px;top:124px;width:100px;font-size:4.3px">Lorem ipsum dolor sit amet, consec- tetur adipiscing elit. Vivamus eget vestibulumex, ut tincidunt nisl.</p>
  <div role="img" aria-label="Regional map with office locations highlighted in blue" style="left:210px;top:40px;width:134px;height:150px;background:linear-gradient(160deg,#d9dce0 0%,#c9cdd3 100%)"></div>
  <svg style="left:210px;top:40px" width="134" height="150" viewBox="0 0 134 150" fill="#1f1f1f">
    <g><circle cx="28" cy="20" r="2.2"/><path d="M26 21 L28 26 L30 21Z"/></g>
    <g><circle cx="118" cy="4" r="2.2"/><path d="M116 5 L118 10 L120 5Z"/></g>
    <g><circle cx="62" cy="48" r="2.2"/><path d="M60 49 L62 54 L64 49Z"/></g>
    <g><circle cx="20" cy="100" r="2.2"/><path d="M18 101 L20 106 L22 101Z"/></g>
    <g><circle cx="56" cy="92" r="2.2"/><path d="M54 93 L56 98 L58 93Z"/></g>
    <g><circle cx="92" cy="112" r="2.2"/><path d="M90 113 L92 118 L94 113Z"/></g>
  </svg>
  <div class="footer-band"></div><span class="footer-note">COPYRIGHT TEXT HERE</span><div class="page-tab"></div><span class="page-num">01</span>
</section>

<!-- Bullet heading here list -->
<section class="slide col3 row4">
  <div class="backdrop" style="left:250px;width:70px"></div>
  <div class="brand small"><span class="brand-mark"></span>BRANNOW</div>
  <h2 class="heading bar" style="left:9px;top:4px;font-size:11px">Bullet <em>heading here</em></h2>
  <div class="bullet-item" style="top:34px"><h4>Bullet Heading here</h4><p>Lorem ipsum dolor sit amet, consectetur adipiscing elit. Vivamus eget vestib Lorem ipsum dolor sit amet, consectetur adipiscing elit. Vivamus eget vestib Vivamus eget vestibVivamus eget vestib Lorem ipsum dolor sit amet, consectetur adipiscing elit. Vivamus eget vestib Lorem ipsum dolor sit amet, consectetur adipiscing elit.</p></div>
  <div class="bullet-item" style="top:86px"><h4>Bullet Heading here</h4><p>Lorem ipsum dolor sit amet, consectetur adipiscing elit. Vivamus eget vestib Lorem ipsum dolor sit amet, consectetur adipiscing elit. Vivamus eget vestib Vivamus eget vestibVivamus eget vestib Lorem ipsum dolor sit amet, consectetur adipiscing elit. Vivamus eget vestib Lorem ipsum dolor sit amet, consectetur adipiscing elit.</p></div>
  <div class="bullet-item" style="top:137px"><h4>Bullet Heading here</h4><p>Lorem ipsum dolor sit amet, consectetur adipiscing elit. Vivamus eget vestib Lorem ipsum dolor sit amet, consectetur adipiscing elit. Vivamus eget vestib Vivamus eget vestibVivamus eget vestib Lorem ipsum dolor sit amet, consectetur adipiscing elit. Vivamus eget vestib Lorem ipsum dolor sit amet, consectetur adipiscing elit.</p></div>
  <div class="footer-band"></div><span class="footer-note">COPYRIGHT TEXT HERE</span><div class="page-tab"></div><span class="page-num">01</span>
</section>

<!-- Line chart -->
<section class="slide col1 row5">
  <div class="brand small"><span class="brand-mark"></span>BRANNOW</div>
  <h2 class="heading flag" style="left:11px;top:3px;font-size:11px"><em>Slide Title</em> Here</h2>
  <svg style="left:0;top:0" width="382" height="214" viewBox="0 0 382 214" font-family="Montserrat,sans-serif" font-size="5.5" fill="#9aa0a7">
    <g stroke="#d4d7dc" stroke-width=".6">
      <line x1="55" y1="58" x2="205" y2="58"/><line x1="55" y1="76" x2="205" y2="76"/><line x1="55" y1="94" x2="205" y2="94"/>
      <line x1="55" y1="104" x2="205" y2="104"/><line x1="55" y1="112" x2="205" y2="112"/><line x1="55" y1="126" x2="205" y2="126"/><line x1="55" y1="148" x2="205" y2="148"/>
    </g>
    <text x="30" y="60">100%</text><text x="35" y="106">50%</text><text x="39" y="150">0%</text>
    <text x="58" y="169">JAN</text><text x="102" y="169">MAR</text><text x="145" y="169">MAY</text><text x="193" y="169">JUL</text>
    <polyline fill="none" stroke="#333a44" stroke-width="1" points="56,112 77,100 96,115 113,100 132,121 150,86 163,115 183,78 200,70 205,74 209,80"/>
    <polyline fill="none" stroke="#1f6fc5" stroke-width="1" points="56,128 77,104 96,100 113,90 132,92 150,102 163,96 183,107 200,105 205,102 209,103"/>
    <g fill="#333a44"><circle cx="77" cy="100" r="1.8"/><circle cx="96" cy="115" r="1.8"/><circle cx="132" cy="121" r="1.8"/><circle cx="163" cy="115" r="1.8"/><circle cx="183" cy="78" r="1.8"/><circle cx="200" cy="70" r="1.8"/><circle cx="209" cy="80" r="1.8"/></g>
    <g fill="#1f6fc5"><circle cx="77" cy="104" r="1.8"/><circle cx="113" cy="90" r="1.8"/><circle cx="150" cy="102" r="1.8"/><circle cx="183" cy="107" r="1.8"/><circle cx="209" cy="103" r="1.8"/></g>
    <rect x="347" y="102" width="5" height="5" fill="#1f6fc5"/><rect x="347" y="153" width="5" height="5" fill="#333a44"/>
    <g fill="#333a44" font-size="5.5" text-anchor="end"><text x="337" y="107">LOREM IPSUM</text><text x="337" y="158">LOREM IPSUM</text></g>
    <g font-size="4.6" text-anchor="end" fill="#7d848d"><text x="337" y="118">Lorem ipsum dolor sit amet,</text><text x="337" y="127">consectetur adipiscing.</text><text x="337" y="169">Lorem ipsum dolor sit amet,</text><text x="337" y="178">consectetur adipiscing.</text></g>
  </svg>
  <div class="footer-band"></div><span class="footer-note">COPYRIGHT TEXT HERE</span><div class="page-tab"></div><span class="page-num">01</span>
</section>

<!-- Consectetur Adipiscing -->
<section class="slide col2 row5">
  <div class="backdrop" style="left:320px;width:50px"></div>
  <div class="brand small"><span class="brand-mark"></span>BRANNOW</div>
  <h2 class="heading" style="left:28px;top:62px;font-size:11.5px;line-height:1.45">Consectetur<br><em>Adipiscing</em></h2>
  <div style="left:28px;top:105px;width:32px;height:1.5px;background:var(--ink)"></div>
  <p class="body-text" style="left:28px;top:118px;width:90px;font-size:4.2px">Lorem ipsA dolor sit amet, conse- ctetur adipiscing elit. Vivamus eget vestibulum ex, ut tinci- dunt nisl. Nunc tortor libero.</p>
  <div class="photo-dart" role="img" aria-label="Darts hitting a dartboard bullseye" style="left:138px;top:0;width:103px;height:93px"></div>
  <div class="blue-block" style="left:163px;top:94px;width:52px;height:27px"></div>
  <div class="photo-paper" role="img" aria-label="Balance sheet with pen and calculator" style="left:138px;top:120px;width:103px;height:94px"></div>
  <h3 style="left:277px;top:54px;font-size:6.2px;font-weight:600">Lorem ipsum</h3>
  <p class="body-text" style="left:277px;top:64px;width:72px;font-size:4.1px">Lorem ipsA dolor sit amet, consectetur adipiscing elit.Vivamus</p>
  <h3 style="left:277px;top:124px;font-size:6.2px;font-weight:600">Lorem ipsum</h3>
  <p class="body-text" style="left:277px;top:134px;width:72px;font-size:4.1px">Lorem ipsA dolor sit amet, consectetur adipiscing elit.Vivamus</p>
  <div class="footer-band"></div><span class="footer-note">COPYRIGHT TEXT HERE</span><div class="page-tab"></div><span class="page-num">01</span>
</section>

<!-- Thank You -->
<section class="slide col3 row5">
  <div class="backdrop" style="left:250px;width:70px"></div>
  <div class="brand" style="left:0;width:100%;top:66px;justify-content:center;font-size:13px;flex-direction:column;gap:3px"><span class="brand-mark" style="width:12px;height:12px"></span>BRANNOW<small style="font-size:4px;letter-spacing:1.5px;font-weight:500">ADVISORY</small></div>
  <h2 class="heading" style="left:0;width:100%;top:104px;text-align:center;font-size:29px">THANK <em>YOU</em></h2>
  <p class="body-text" style="left:0;width:100%;top:146px;text-align:center;font-size:6px;color:var(--ink);line-height:1.45">Lorem ipsum dolor sit amet, consectetur<br>adipiscing elit vivamus eget.</p>
  <p style="left:0;width:100%;top:171px;text-align:center;font-size:5.2px;color:var(--blue)">https://brannowadvisory.com/</p>
  <div class="footer-band"></div><span class="footer-note">COPYRIGHT TEXT HERE</span><div class="page-tab"></div><span class="page-num">01</span>
</section>

</body>
</html>
```